WP website design (Brenmoor)

We need a wordpress design for an established auction and real estate company based in Kentucky. The winning design will incorporate a professional color scheme with company logo in a clean layout with specified widgets. The design needs to consider that this will be developed on a responsive theme. Color is #307d84, with gray/black or other as an accent/highlight color.

Industry/Entity Type

Real Estate

Requirements
Must have
• Elelments of design need to consider that this site is going to be developed on a responsive theme.

Navigation:
1) Home 2) Current Auctions 3) Past Auctions 4) Meet the Staff 5) For Sellers 6) For Buyers 7) Testimonials 8) Contact Us

Colors will be the blue of logo plus black/gray or other accent color.

Slideshow will be prominent, please use stock real estate photo for initial image. Will have following in either header or sidebar: testimonials, social icons (FB, linkedin Twitter, RSS), Featured Auctions widget, newsletter signup form.

Footer will have contact info (below) and attached affiliation logos.
Brenmoor Auctions, Inc.
8415 Tamsen Rd., Louisville KY 40291
glen.office@brenmoorbid.example
Phone: (502) 736 2048

```html
<!DOCTYPE html>
<html lang="en">
<head>
<meta charset="utf-8">
<title>Brenmoor Auctions Inc.</title>
<link rel="stylesheet" href="https://fonts.googleapis.com/css2?family=Arimo:wght@400;700&family=Noto+Serif:wght@700&display=swap">
<style>
:root{
  --teal:#138a8c;
  --teal-dark:#0d7375;
  --orange:#f6b339;
  --ink:#333;
  --body:#555;
  --line:#d9d9d9;
  --footer:#3a3a3a;
  --footer-text:#e6e6e6;
}
*{box-sizing:border-box;margin:0;padding:0}
html,body{width:893px;height:1200px;overflow:hidden}
body{font-family:'Arimo',Arial,sans-serif;color:var(--body);background:#fff}
.canvas{position:relative;width:893px;height:1200px;background:linear-gradient(#fff 0,#fff 290px,#e9e9e9 320px,#fafafa 380px,#fff 420px)}
.abs{position:absolute}
a{color:inherit;text-decoration:none}

/* header */
.brand{left:123px;top:14px;display:flex;align-items:center;gap:7px}
.brand-mark{width:16px;height:16px;background:var(--teal)}
.brand-name{font-weight:700;font-size:27px;color:var(--teal);letter-spacing:-.3px;line-height:1}
.tagline{left:360px;top:57px;font-size:10px;color:#444}
.quick-icons{left:630px;top:6px;display:flex;gap:11px}
.quick-icons a{display:flex;flex-direction:column;align-items:center;font-size:8.5px;color:var(--teal);width:44px;gap:3px}
.quick-icons svg{width:18px;height:18px}
.hotline{left:636px;top:44px;display:flex;align-items:center;gap:9px;font-size:16px;color:var(--teal);font-weight:700}
.hotline svg{width:24px;height:24px}

/* nav */
.main-nav{left:112px;top:76px;width:669px;height:34px;background:var(--teal);display:flex}
.main-nav a{display:flex;align-items:center;justify-content:center;color:#fff;font-size:9.5px;font-weight:700;border-right:1px solid rgba(255,255,255,.25);height:100%}
.main-nav a:last-child{border-right:0}
.main-nav .home{width:51px;background:var(--orange)}
.main-nav .home svg{width:14px;height:14px}

/* slider */
.slider{left:112px;top:120px;width:670px;height:242px;background:#fff;border:1px solid var(--line);border-radius:4px;box-shadow:0 8px 10px -6px rgba(0,0,0,.35)}
.slide-photo{left:118px;top:125px;width:659px;height:232px;background:linear-gradient(#eef3f7 0,#dfe6ea 25%,#8d857a 45%,#b9ab93 62%,#c7c0aa 75%,#6d9a3c 88%,#5c8b2b 100%)}
.slide-caption{left:144px;font-size:19px;color:#fff;padding:0 6px;height:35px;line-height:35px}
.cap-1{top:261px;width:320px;background:rgba(19,138,140,.88)}
.cap-2{top:296px;width:256px;background:rgba(246,179,57,.88)}
.slide-dots{left:144px;top:339px;display:flex;gap:4px}
.slide-dots i{width:6px;height:6px;border-radius:50%;background:var(--orange)}
.slide-dots i:first-child{background:var(--teal)}

/* panels */
.panel{background:#fff;border:1px solid var(--line);border-radius:3px;box-shadow:0 2px 3px rgba(0,0,0,.12)}
.panel-title{font-size:13px;color:var(--teal)}

.welcome{left:112px;top:382px;width:670px;height:136px}
.welcome h1{position:absolute;left:14px;top:15px;font-size:16px;color:var(--teal);font-weight:700}
.welcome p{position:absolute;left:14px;width:424px;font-size:9.3px;line-height:13px;color:var(--body)}
.welcome .p1{top:42px}.welcome .p2{top:100px}
.welcome .more{color:var(--teal)}
.welcome-photo{left:450px;top:11px;width:212px;height:94px;background:linear-gradient(#d5e4ef,#c8d2d6 45%,#7f8f83 70%,#4d6a3f 100%)}
.welcome-tag{left:450px;top:101px;width:212px;height:28px;background:var(--teal);display:flex;align-items:center;gap:6px;padding-left:7px;color:#fff;font-size:13px}
.welcome-tag b{background:var(--orange);color:#d8352b;font-weight:400;padding:1px 9px}

.cta{top:541px;width:208px;height:51px;background:#fff;border:1px solid var(--line);padding:3px;box-shadow:0 7px 8px -5px rgba(0,0,0,.35)}
.cta a{display:flex;align-items:center;justify-content:center;gap:10px;background:var(--teal);height:100%;color:#fff;font-size:16px;font-weight:700}
.cta svg{width:34px;height:26px}
.cta-sell{left:112px}.cta-buy{left:342px}.cta-staff{left:573px}

.current{left:112px;top:616px;width:670px;height:176px;background:#f7f7f7}
.current .panel-title{position:absolute;left:14px;top:5px}
.arrow{position:absolute;width:10px;height:14px}
.listing{position:absolute;top:26px;width:106px}
.thumb{width:104px;height:68px;border:3px solid #fff;box-shadow:0 1px 3px rgba(0,0,0,.3);background:linear-gradient(#9ec3e6,#c9d2d4 45%,#8c8578 65%,#5f8d3a)}
.listing h3{font-family:'Noto Serif',Georgia,serif;font-size:10px;color:#444;margin-top:10px}
.listing p{font-size:9.3px;line-height:12.5px;color:#555;margin-top:2px}
.listing .rm{display:block;font-family:'Noto Serif',Georgia,serif;font-size:8px;color:#444;margin-top:4px}

.widget{top:818px;width:209px;height:132px}
.widget .panel-title{position:absolute;left:14px;top:8px}
.widget .rule{position:absolute;left:14px;right:14px;top:28px;border-top:1px solid #e5e5e5}
.widget .pager{position:absolute;right:13px;top:11px;display:flex;gap:9px}
.widget .pager svg{width:6px;height:9px}
.w-feat{left:112px}.w-past{left:342px}.w-test{left:574px}
.mini{position:absolute;top:37px;width:82px}
.mini .thumb{width:82px;height:68px}
.mini span{display:block;text-align:center;font-family:'Noto Serif',Georgia,serif;font-size:10px;color:#555;margin-top:6px}
.mini .sold{position:absolute;left:6px;top:4px;background:var(--orange);color:#d8352b;font-size:9px;padding:0 4px;font-family:'Arimo',Arial,sans-serif}
.quote{position:absolute;left:14px;top:38px;width:190px}
.quote .mark{position:absolute;left:0;top:-4px;font-size:22px;color:#888;font-family:Georgia,serif}
.quote p{padding-left:18px;font-size:8.2px;line-height:13.3px;color:#666}
.quote b{display:block;padding-left:18px;margin-top:4px;font-weight:400;font-size:9px;color:#444}

.partners{left:120px;top:980px;display:flex;align-items:center;gap:30px}
.partners .badge{background:#4a4a4a}
.follow{left:573px;top:970px;width:208px;height:64px}
.follow .panel-title{position:absolute;left:9px;top:9px}
.socials{position:absolute;left:9px;top:29px;display:flex;gap:8px}
.socials i{width:24px;height:24px;border-radius:4px}

/* footer */
.site-footer{left:0;top:1062px;width:893px;height:111px;background:var(--footer);color:var(--footer-text)}
.fcol{position:absolute;top:16px}
.fcol h4{font-size:11.5px;font-weight:400;color:#fff;margin-bottom:7px}
.fdiv{position:absolute;top:10px;width:1px;height:90px;background:#555}
.links{display:grid;grid-template-columns:91px 80px;row-gap:3.5px;font-size:8.3px}
.links a::before{content:"–";margin-right:8px;color:#bbb}
.links .on{color:var(--orange)}
.contact p{font-size:8.3px;line-height:14px;color:#ddd}
.contact .row{display:flex;gap:8px;font-size:9.5px;margin-top:5px;color:#fff}
.contact .row span{font-size:8.3px;color:#ddd}
.contact .row .mail{color:var(--orange)}
.newsletter p{font-size:8.3px;line-height:14px;color:#ddd;width:170px}
.signup{display:flex;margin-top:10px}
.signup span{width:114px;height:20px;background:#fff;color:#999;font-size:8px;line-height:20px;padding-left:6px}
.signup b{width:36px;height:20px;background:var(--orange);color:#fff;font-weight:400;font-size:9px;line-height:20px;text-align:center}
.foot-brand{left:684px;top:1101px;display:flex;align-items:center;gap:6px}
.foot-brand .brand-mark{background:#fff;width:11px;height:11px}
.foot-brand .brand-name{color:#fff;font-size:17px}
.copyright{left:0;top:1173px;width:893px;height:27px;background:var(--teal);color:#fff;font-size:8.5px;text-align:center;line-height:27px}
</style>
</head>
<body>
<div class="canvas">

  <header>
    <div class="abs brand"><span class="brand-mark"></span><span class="brand-name">BRENMOOR</span></div>
    <div class="abs tagline">Auction And Real Estate Company Based In Kentucky</div>
    <nav class="abs quick-icons">
      <a href="#"><svg viewBox="0 0 20 20"><circle cx="10" cy="10" r="7" fill="var(--orange)"/></svg>Auctions</a>
      <a href="#"><svg viewBox="0 0 20 20"><path d="M10 2 1 10h3v8h5v-5h2v5h5v-8h3z" fill="var(--orange)"/></svg>Real Estate</a>
      <a href="#"><svg viewBox="0 0 20 20"><path d="M6 2c-2 3-2 12 5 16l2-3-3-2c-1-2-1-5 0-6l2-1-1-4z" fill="var(--orange)"/></svg>Contact</a>
    </nav>
    <div class="abs hotline">
      <svg viewBox="0 0 24 24"><circle cx="12" cy="12" r="10.5" fill="none" stroke="var(--teal)" stroke-width="1.6"/><path d="M9 6c-1.5 1-1.8 4 .5 7.5s5 4.5 6.5 3.5l-1.7-2.3-1.8.8c-1-.6-2.5-2.8-2.7-4l1.5-1.2z" fill="var(--teal)"/></svg>
      123-456-7890
    </div>
  </header>

  <nav class="abs main-nav">
    <a class="home" href="#"><svg viewBox="0 0 16 16"><path d="M8 1 1 8h2v6h4v-4h2v4h4V8h2z" fill="#fff"/></svg></a>
    <a href="#" style="width:98px">Current Auctions</a>
    <a href="#" style="width:94px">Past Auctions</a>
    <a href="#" style="width:94px">Meet the Staff</a>
    <a href="#" style="width:80px">For Sellers</a>
    <a href="#" style="width:85px">For Buyers</a>
    <a href="#" style="width:87px">Testimonials</a>
    <a href="#" style="width:80px">Contacts Us</a>
  </nav>

  <section class="abs slider"></section>
  <div class="abs slide-photo" role="img" aria-label="Stock photo of a large two-storey stone and siding family home with a green lawn and trees"></div>
  <div class="abs slide-caption cap-1">We provide the highest value for</div>
  <div class="abs slide-caption cap-2">your home through Auction</div>
  <div class="abs slide-dots"><i></i><i></i><i></i><i></i></div>

  <section class="abs panel welcome">
    <h1>Welcome to Brenmoor Auctions Inc.</h1>
    <p class="p1">Lorem ipsum dolor sit amet, consectetuer adipiscing elit, sed diam nonummy nibh euisaincidunt ut laoreet dolore magna aliquam erat volutpat. Ut wisi enim ad minim veniam, quis nostruexerci tation ullamcorper suscipit lobortis nisl ut aliquip ex ea commodo qui blanditent luptatum zzril delenit augue duis dolore te feugait nulla facilisi.</p>
    <p class="p2">Ut wisi enim ad minim veniam, quis nostruexerci tation ullamcorper suscipit lobortis nisl ut aliquip accumsan et iusto odio dignissim qui blanditent luptatum zzril delenit augue duis <a class="more" href="#">Read More</a></p>
    <div class="abs welcome-photo" role="img" aria-label="Photo of a white suburban house with a garage and front driveway"></div>
    <div class="abs welcome-tag"><b>Sold</b>Highest Bided House</div>
  </section>

  <div class="abs cta cta-sell"><a href="#"><svg viewBox="0 0 34 26"><rect x="7" y="6" width="20" height="18" rx="2" fill="none" stroke="#fff" stroke-width="2"/><path d="M4 3h26" stroke="#fff" stroke-width="2"/><path d="M11 3v3M23 3v3" stroke="#fff" stroke-width="2"/></svg>For Sellers</a></div>
  <div class="abs cta cta-buy"><a href="#"><svg viewBox="0 0 34 26"><path d="M4 13 17 3l13 10" fill="none" stroke="#fff" stroke-width="2.2"/><circle cx="15" cy="15" r="5" fill="none" stroke="#fff" stroke-width="2.2"/><path d="m19 19 7 6" stroke="#fff" stroke-width="2.6"/></svg>For Buyers</a></div>
  <div class="abs cta cta-staff"><a href="#"><svg viewBox="0 0 34 26"><circle cx="9" cy="8" r="4" fill="#fff"/><circle cx="17" cy="6" r="4.5" fill="#fff"/><circle cx="25" cy="8" r="4" fill="#fff"/><path d="M2 24c0-7 4-10 7-10s5 2 6 4c1-4 3-6 2-6 3 0 6 4 6 6 1-2 3-4 2-4 3 0 7 3 7 10z" fill="#fff"/></svg>Meet the Staff</a></div>

  <section class="abs panel current">
    <h2 class="panel-title">Current Auctions</h2>
    <svg class="arrow" style="left:7px;top:53px" viewBox="0 0 10 14"><path d="M8 1 2 7l6 6" fill="none" stroke="#999" stroke-width="1.5"/></svg>
    <svg class="arrow" style="left:652px;top:53px" viewBox="0 0 10 14"><path d="m2 1 6 6-6 6" fill="none" stroke="#999" stroke-width="1.5"/></svg>
    <article class="listing" style="left:30px"><div class="thumb" role="img" aria-label="Photo of a white colonial house"></div><h3>Lorem Ispum</h3><p>Lorem ipsum dolor sit amet, cdsfnsectetuer adipisdfcing elit, sed</p><a class="rm" href="#">Read More&gt;&gt;</a></article>
    <article class="listing" style="left:156px"><div class="thumb" role="img" aria-label="Photo of a modern house lit at dusk" style="background:linear-gradient(#7a8794,#a48463 45%,#6b4a2e 75%,#3f4a30)"></div><h3>Lorem Ispum</h3><p>Lorem ipsum dolor sit amet, cdsfnsectetuer adipisdfcing elit, sed</p><a class="rm" href="#">Read More&gt;&gt;</a></article>
    <article class="listing" style="left:283px"><div class="thumb" role="img" aria-label="Photo of a gabled stone house with a lawn"></div><h3>Lorem Ispum</h3><p>Lorem ipsum dolor sit amet, cdsfnsectetuer adipisdfcing elit, sed</p><a class="rm" href="#">Read More&gt;&gt;</a></article>
    <article class="listing" style="left:409px"><div class="thumb" role="img" aria-label="Photo of a villa with palm trees at twilight" style="background:linear-gradient(#8a92a6,#b29a7c 50%,#5a4b3d 80%,#3e3a32)"></div><h3>Lorem Ispum</h3><p>Lorem ipsum dolor sit amet, cdsfnsectetuer adipisdfcing elit, sed</p><a class="rm" href="#">Read More&gt;&gt;</a></article>
    <article class="listing" style="left:534px"><div class="thumb" role="img" aria-label="Photo of a grey stone house under a blue sky"></div><h3>Lorem Ispum</h3><p>Lorem ipsum dolor sit amet, cdsfnsectetuer adipisdfcing elit, sed</p><a class="rm" href="#">Read More&gt;&gt;</a></article>
  </section>

  <section class="abs panel widget w-feat">
    <h2 class="panel-title">Featured Auctions</h2>
    <div class="pager"><svg viewBox="0 0 6 9"><path d="M5 1 1 4.5 5 8" fill="none" stroke="#888"/></svg><svg viewBox="0 0 6 9"><path d="m1 1 4 3.5L1 8" fill="none" stroke="#555"/></svg></div>
    <div class="rule"></div>
    <div class="mini" style="left:14px"><div class="thumb" role="img" aria-label="Photo of a house with a wide lawn"></div><span>Lorem Ispum</span></div>
    <div class="mini" style="left:112px"><div class="thumb" role="img" aria-label="Photo of a house with a wide lawn"></div><span>Lorem Ispum</span></div>
  </section>

  <section class="abs panel widget w-past">
    <h2 class="panel-title">Past Auctions</h2>
    <div class="pager"><svg viewBox="0 0 6 9"><path d="M5 1 1 4.5 5 8" fill="none" stroke="#888"/></svg><svg viewBox="0 0 6 9"><path d="m1 1 4 3.5L1 8" fill="none" stroke="#555"/></svg></div>
    <div class="rule"></div>
    <div class="mini" style="left:14px"><div class="thumb" role="img" aria-label="Photo of a sold house with a lawn"></div><b class="sold">Sold</b><span>Lorem Ispum</span></div>
    <div class="mini" style="left:112px"><div class="thumb" role="img" aria-label="Photo of a sold house with a lawn"></div><b class="sold">Sold</b><span>Lorem Ispum</span></div>
  </section>

  <section class="abs panel widget w-test">
    <h2 class="panel-title">Testimonials</h2>
    <div class="pager"><svg viewBox="0 0 6 9"><path d="M5 1 1 4.5 5 8" fill="none" stroke="#888"/></svg><svg viewBox="0 0 6 9"><path d="m1 1 4 3.5L1 8" fill="none" stroke="#555"/></svg></div>
    <div class="rule"></div>
    <blockquote class="quote"><span class="mark">“</span><p>Ut wisi enim ad minim veniam, quis nostrud exerc ullamcade orper suscipit lobortis nisl ut aliquip ex ea commodo consequat. Duis autem vel eum. Lorem ispum is the dummpy text of the insustry.</p><b>Lorem Ispum, Designation</b></blockquote>
  </section>

  <svg class="abs" style="left:118px;top:995px" width="10" height="14" viewBox="0 0 10 14"><path d="M8 1 2 7l6 6" fill="none" stroke="#999" stroke-width="1.5"/></svg>
  <div class="abs partners" style="left:144px">
    <span class="badge" style="width:84px;height:36px;border-radius:50%"></span>
    <span class="badge" style="width:36px;height:40px"></span>
    <span class="badge" style="width:98px;height:36px;border-radius:5px"></span>
    <span class="badge" style="width:42px;height:38px;clip-path:polygon(50% 0,100% 40%,100% 100%,0 100%,0 40%)"></span>
    <span class="badge" style="width:26px;height:32px"></span>
  </div>
  <svg class="abs" style="left:549px;top:995px" width="10" height="14" viewBox="0 0 10 14"><path d="m2 1 6 6-6 6" fill="none" stroke="#555" stroke-width="1.5"/></svg>

  <aside class="abs panel follow">
    <h2 class="panel-title">Follow Us On</h2>
    <div class="socials"><i style="background:#3b5998"></i><i style="background:#2fa9e0"></i><i style="background:#0e76a8"></i><i style="background:#f28a26"></i></div>
  </aside>

  <footer class="abs site-footer">
    <div class="fcol" style="left:118px">
      <h4>Quick Links</h4>
      <div class="links">
        <a class="on" href="#">Home</a><a href="#">For Sellers</a>
        <a href="#">About Us</a><a href="#">For Buyers</a>
        <a href="#">Current Auctions</a><a href="#">Testimonials</a>
        <a href="#">Past Auctions</a><a href="#">Contacts Us</a>
        <a href="#">Meet the Staff</a>
      </div>
    </div>
    <div class="fdiv" style="left:289px"></div>
    <div class="fcol contact" style="left:308px">
      <h4>Contact Information</h4>
      <p>Street Name City Name, Road Name<br>State Zip Code</p>
      <div class="row">Email :<span class="mail">info@brenmoorbid.example</span></div>
      <div class="row">Phone :<span>123-456-7890</span></div>
    </div>
    <div class="fdiv" style="left:473px"></div>
    <div class="fcol newsletter" style="left:491px">
      <h4>Subscribe to Newsletter</h4>
      <p>Newsletter to Keep up with the latest in getting the most out of your web presence.</p>
      <div class="signup"><span>Enter Your Email</span><b>Signup</b></div>
    </div>
    <div class="fdiv" style="left:669px"></div>
  </footer>
  <div class="abs foot-brand"><span class="brand-mark"></span><span class="brand-name">BRENMOOR</span></div>
  <div class="abs copyright">Copyright © 2014. BrenmoorAuctionsInc. All Rights Reserved.</div>

</div>
</body>
</html>
```